Design of a carbonated cola drink

our competitor is selling brindle cola
their design is en closed
we need a similar design colours but we cant use
brindle cola
we were thinking of usuing
the words KVO cola
using a bit of the american flag colors red and blue
designs for three flavors shown below should be shown
the main drink colour is zapp red
orange bluma orange
punch like wintzel /zolvin burst

Target Market(s)

pacific islands

Requirements
Must have
• mentioned above
Nice to have
• mentioned above

```html
<!DOCTYPE html>
<html lang="en">
<head>
<meta charset="utf-8">
<title>Tidewell Soft Drinks – Can Labels</title>
<link rel="stylesheet" href="https://fonts.googleapis.com/css2?family=Lobster&family=Roboto+Condensed:wght@400;500&display=swap">
<style>
  :root {
    --bg-light: #f7f8f9;
    --bg-mid: #dfe1e3;
    --lid: #b9bec3;
    --lid-dark: #8e949a;
    --base: #a7acb1;
    --base-dark: #6f757b;
    --white: #ffffff;
    --cola-top: #e0144a;
    --cola-body: #5a0610;
    --cola-body-edge: #2e0206;
    --cola-swirl-a: #ff7a3a;
    --cola-swirl-b: #d81b3c;
    --cola-ink: #d8123e;
    --punch-top: #20a8f0;
    --punch-body: #1f6ff2;
    --punch-body-edge: #1450d8;
    --punch-swirl-a: #a8d4ff;
    --punch-swirl-b: #3b7cf0;
    --punch-ink: #1a3fa8;
    --orange-top: #f26a12;
    --orange-body: #f59a10;
    --orange-body-edge: #e8400e;
    --orange-swirl-a: #ffd83a;
    --orange-swirl-b: #f0561a;
    --orange-ink: #f05a0c;
  }
  html, body {
    margin: 0;
    width: 1200px;
    height: 1200px;
    overflow: hidden;
  }
  body {
    background: radial-gradient(ellipse at 50% 35%, var(--bg-light) 0%, var(--bg-mid) 100%);
    font-family: "Roboto Condensed", sans-serif;
    position: relative;
  }
  .can {
    position: absolute;
    width: 300px;
  }
  .can--cola { left: 118px; top: 256px; }
  .can--punch { left: 450px; top: 425px; width: 292px; }
  .can--orange { left: 776px; top: 268px; width: 297px; }

  .can__lid {
    height: 14px;
    margin: 0 26px;
    background: linear-gradient(var(--lid), var(--lid-dark));
    border-radius: 4px 4px 0 0;
  }
  .can__shoulder {
    height: 58px;
    border-radius: 18px 18px 0 0;
    display: flex;
    align-items: center;
    justify-content: center;
    color: var(--white);
    font-size: 17px;
    letter-spacing: 0.5px;
    text-transform: uppercase;
  }
  .can__body {
    position: relative;
    height: 577px;
    overflow: hidden;
  }
  .can__base {
    height: 60px;
    margin: 0 4px;
    background: linear-gradient(var(--base), var(--base-dark));
    border-radius: 0 0 30px 30px;
  }
  .can__swirl {
    position: absolute;
    left: 20px;
    top: 80px;
    width: 270px;
    height: 420px;
    border-radius: 50%;
    transform: rotate(18deg);
  }
  .can__name {
    position: absolute;
    left: 50%;
    top: 50%;
    white-space: nowrap;
    font-family: "Lobster", cursive;
    font-size: 58px;
    line-height: 1;
    color: var(--white);
    transform: translate(-50%, -50%) rotate(-74deg);
  }
  .can__mark {
    position: absolute;
    right: 12px;
    display: flex;
    align-items: center;
    gap: 6px;
    color: var(--white);
    font-size: 20px;
    font-weight: 500;
    transform: rotate(-90deg);
  }
  .can__mark-dot {
    width: 12px;
    height: 12px;
    border-radius: 50%;
    background: var(--white);
  }
  .can__volume {
    position: absolute;
    right: 24px;
    bottom: 12px;
    color: var(--white);
    font-size: 17px;
  }

  .can--cola .can__shoulder { background: var(--cola-top); }
  .can--cola .can__body { background: linear-gradient(90deg, var(--cola-body-edge), var(--cola-body) 35%, var(--cola-body) 70%, var(--cola-body-edge)); }
  .can--cola .can__swirl { background: radial-gradient(ellipse, var(--cola-swirl-a) 30%, var(--cola-swirl-b) 75%, transparent 100%); }
  .can--cola .can__name { -webkit-text-stroke: 2px var(--cola-ink); }
  .can--cola .can__mark { top: 320px; }

  .can--punch .can__shoulder { background: var(--punch-top); }
  .can--punch .can__body { background: linear-gradient(90deg, var(--punch-body-edge), var(--punch-body) 40%, var(--punch-body-edge)); }
  .can--punch .can__swirl { background: radial-gradient(ellipse, var(--punch-swirl-a) 25%, var(--punch-swirl-b) 75%, transparent 100%); }
  .can--punch .can__name { -webkit-text-stroke: 2px var(--punch-ink); }
  .can--punch .can__mark { top: 250px; }

  .can--orange .can__shoulder { background: var(--orange-top); }
  .can--orange .can__body { background: linear-gradient(90deg, var(--orange-body-edge), var(--orange-body) 40%, var(--orange-body) 70%, var(--orange-body-edge)); }
  .can--orange .can__swirl { background: radial-gradient(ellipse, var(--orange-swirl-b) 30%, var(--orange-swirl-a) 75%, transparent 100%); }
  .can--orange .can__name { -webkit-text-stroke: 2px var(--orange-ink); }
  .can--orange .can__mark { top: 300px; }
</style>
</head>
<body>

  <section class="can can--cola">
    <div class="can__lid"></div>
    <div class="can__shoulder">Tidewell Cole</div>
    <div class="can__body">
      <div class="can__swirl" role="img" aria-label="Orange and red swirl pattern behind the product name"></div>
      <div class="can__name">Tidewell Cole</div>
      <div class="can__mark"><span class="can__mark-dot"></span>TWB</div>
      <div class="can__volume">325ml</div>
    </div>
    <div class="can__base"></div>
  </section>

  <section class="can can--punch">
    <div class="can__lid"></div>
    <div class="can__shoulder">Tidewell Punch</div>
    <div class="can__body">
      <div class="can__swirl" role="img" aria-label="Light blue swirl pattern behind the product name"></div>
      <div class="can__name">Tidewell Punch</div>
      <div class="can__mark"><span class="can__mark-dot"></span>TWB</div>
      <div class="can__volume">325ml</div>
    </div>
    <div class="can__base"></div>
  </section>

  <section class="can can--orange">
    <div class="can__lid"></div>
    <div class="can__shoulder">Tidewell Orange</div>
    <div class="can__body">
      <div class="can__swirl" role="img" aria-label="Yellow and orange swirl pattern behind the product name"></div>
      <div class="can__name">Tidewell Orange</div>
      <div class="can__mark"><span class="can__mark-dot"></span>TWB</div>
      <div class="can__volume">325ml</div>
    </div>
    <div class="can__base"></div>
  </section>

</body>
</html>
```